Wordpress Website for Waikiki based Boutique Retail Commercial Realestate Company

Aloha!
We need a wordpress design for a new company based in Waikiki, Oahu. I am an experienced real estate professional leaving a large national firm to open a boutique agency. I have several colleagues that work for these type of boutique companies on the mainland - and all seemingly have similar type Wordpress websites. Below are the examples I'd like you to use as a starting point but I would like to differentiate ourselves because of our unique position of being located on a tropical island. The design should communicate elegance, sophistication, experience and market knowledge. The photos should all be of Hawaii and Waikiki.

Here are the websites I'd like this to be similar to (but smaller since I am currently a one woman company):
http://www.plv.example/
http://marlowegroupe.example/
http://www.brannockco.example/
(this one is residential real estate, which I don't do but still like this look): http://www.coraldwell.example/

I am not that tech savy but I do own my domain, have it hosted and have had the hosting company install the necessary Wordpress component on to the account.

I would like to form a relationship with a designer that can grow with me so as I want to add features in the future, I can continue to hire you. If you are strictly a designer, that is ok, but I am also looking for someone to do regular administrative work on the website by uploading new information to it regularly.

Also, would you advise me on how to "upload" it to the hosting company?

Aloha Designers,

Here are examples of the interactive map that I'd like to do for my living resume. Instead of an image, however, I'd like it to be over an aerial from Google Earth of Waikiki:

http://www.grandlagoonarcade.example/
http://www.shorelinepromenade.example/

Hope this answers some questions. I look forward to your designs! Mahalo, Marielle

Target Market(s)

upscale & luxury retailers as well as owners of property in Waikiki

Industry/Entity Type

Real Estate

Requirements
Must have
• I need to have the web page coded so I can upload and have a working live web page.

Here is the unique element I'd like to have on my webpage:

I'd like to have a map of Waikiki (Google earth image) that has roll-overs on it. This will be my living, breathing resume. So when someone visits my website, they can roll-over the map and the name of a property will pop-up. They can expand on it to learn more about the work I've done on that property. Don't worry, I'll provide you will all the detail but I'd like to see a sample of how you would handle this.

The only design idea that I've had or thought to play with would be to have the website all in shades of grey except for whatever is being featured - so if there is a large photo - everything would be grey except for the subject building. I don't know if there is an easy Photoshop or software way to do this, and if not, then skip the idea because it would be too labor intensive for lots of photos.

Below is all the typical pages a company like me would have:
Landing Page - full photo images
Assignments/Listings Page
Services Page - this page might have the map described above
News Page
(I'd like to be able to either have this connect to RSS/Twitter/FB. I basically want to take local news articles and upload them here. I will also have an admin person email blast these to my clients once a week in the future. I need some capture system here for people to sign up to receive the news by email, sign up to receive available listings or sign up to participate in future surveys of Waikiki- I'm about to launch one in a week or two).

Contact Page
Nice to have
• Client Access Only Page-
With this page, I'd like to have the ability to control who has access to this page.

It should require their email and password.
It should show the files in PDF format (like the link below)
It should allow them to download the file.
It should send me an email every time someone access this Client Page.

http://www.kelvanorshops.example/catalog-leasing-2011.html

```html
<!DOCTYPE html>
<html lang="en">
<head>
<meta charset="utf-8">
<title>Reyland &amp; Co — Real Estate Boutique</title>
<link rel="stylesheet" href="https://fonts.googleapis.com/css2?family=Gelasio:ital,wght@1,400&family=PT+Sans:ital,wght@0,400;0,700;1,400;1,700&display=swap">
<style>
  :root {
    --nav-bg: #2c2d42;
    --nav-top: #5a5a66;
    --nav-text: #e8e8f0;
    --accent-blue: #3440a8;
    --body-text: #555560;
    --dark-text: #222228;
    --panel-veil: rgba(226, 228, 238, 0.72);
    --card-bg: #ffffff;
    --footer-bg: #e6e6e6;
    --footer-text: #6a6a6a;
    --logo-grey: #8d8f98;
  }
  * { box-sizing: border-box; margin: 0; padding: 0; }
  html, body { width: 1200px; height: 934px; overflow: hidden; background: #fff; }
  body { font-family: "PT Sans", "Helvetica Neue", Arial, sans-serif; color: var(--body-text); position: relative; }
  a { text-decoration: none; }

  .site-header {
    position: absolute; left: 0; top: 0; width: 1200px; height: 86px;
    background: var(--nav-bg); border-top: 2px solid var(--nav-top); z-index: 3;
  }
  .brand {
    position: absolute; left: 141px; top: 0; width: 215px; height: 174px; z-index: 5;
    background: linear-gradient(135deg, #ffffff 0%, #ececef 60%, #dcdce2 100%);
    box-shadow: 0 2px 6px rgba(0,0,0,0.35);
    display: flex; align-items: flex-end; justify-content: center; padding-bottom: 6px;
    text-decoration: none;
  }
  .brand-name { font-size: 21px; color: var(--logo-grey); font-weight: 400; letter-spacing: 0.3px; text-decoration: none; }
  .brand-square { position: absolute; left: 80px; top: 28px; width: 54px; height: 54px; background: var(--logo-grey); }

  .main-nav { position: absolute; left: 461px; top: 32px; display: flex; align-items: center; }
  .main-nav a { color: var(--nav-text); font-size: 13.5px; }
  .main-nav .sep { color: var(--nav-text); font-size: 13.5px; margin: 0 17px; }
  .main-nav .current {
    display: inline-block; width: 63px; height: 31px; line-height: 31px; text-align: center;
    background: linear-gradient(#b8b8c0, #8a8a94); color: #fff; font-weight: 700; border-radius: 2px; margin-right: 20px;
  }

  .hero {
    position: absolute; left: 0; top: 86px; width: 1200px; height: 555px;
    background:
      radial-gradient(ellipse 380px 220px at 150px 470px, #c2a64a 0%, rgba(120,130,60,0.6) 45%, transparent 75%),
      radial-gradient(ellipse 420px 160px at 560px 220px, rgba(240,200,120,0.55) 0%, transparent 70%),
      linear-gradient(180deg, #2a3aa0 0%, #3a55c0 35%, #4a5890 55%, #2e3a48 75%, #1e2a24 100%);
  }
  .slider-dots { position: absolute; left: 981px; top: 103px; display: flex; gap: 6px; z-index: 4; }
  .slider-dots span { width: 15px; height: 15px; border-radius: 50%; background: rgba(200,205,235,0.75); }
  .slider-dots span.active { background: #fff; }

  .featured {
    position: absolute; left: 366px; top: 362px; width: 702px; height: 290px;
    background: var(--panel-veil); z-index: 2;
  }
  .featured h2 {
    position: absolute; left: 12px; top: 10px; font-family: "Gelasio", Georgia, serif; font-style: italic;
    font-weight: 400; font-size: 24px; color: var(--dark-text);
  }
  .property-card {
    position: absolute; top: 51px; width: 215px; height: 239px; background: var(--card-bg); text-align: center;
  }
  .property-card .photo { display: block; margin: 11px auto 0; width: 195px; height: 139px; border: 2px solid #d8d8dc; }
  .property-card h3 { font-size: 15px; font-weight: 700; color: var(--accent-blue); margin-top: 9px; }
  .property-card p { font-size: 12.5px; font-style: italic; color: #555; line-height: 20px; margin-top: 2px; padding: 0 18px; }
  .property-card .details { display: block; font-size: 12.5px; color: var(--dark-text); margin-top: 5px; }
  .card-1 { left: 10px; } .card-2 { left: 244px; } .card-3 { left: 478px; }
  .photo-terrace { background: linear-gradient(180deg, #6aa0d8 0%, #9a7a5a 40%, #c89a68 70%, #5a6a58 100%); }
  .photo-skyline { background: linear-gradient(180deg, #a8a8b0 0%, #8c96a0 50%, #68c8c0 80%, #8ad8d0 100%); }
  .photo-beach { background: linear-gradient(180deg, #3c7cd8 0%, #9ac0e8 35%, #c8c0b0 55%, #30b8c8 80%, #1aa0b8 100%); }

  .intro { position: absolute; top: 652px; left: 0; width: 1200px; height: 223px; }
  .intro h2 {
    font-family: "Gelasio", Georgia, serif; font-style: italic; font-weight: 400; font-size: 24px; line-height: 30px; color: var(--accent-blue);
  }
  .col { position: absolute; top: 43px; height: 170px; }
  .col p { font-size: 12.5px; line-height: 22.5px; margin-top: 7px; }
  .col-welcome { left: 141px; width: 420px; }
  .col-news { left: 609px; width: 210px; }
  .col-news p { line-height: 20px; margin-top: 9px; }
  .col-testimonials { left: 856px; width: 205px; }
  .col-testimonials blockquote { font-size: 12.5px; font-style: italic; line-height: 20px; margin-top: 9px; }
  .quote-mark { font-family: "Gelasio", Georgia, serif; font-style: normal; font-size: 38px; color: #a8a8b0; line-height: 14px; vertical-align: -14px; margin-right: 6px; }
  .col-testimonials cite { display: block; text-align: right; font-size: 12.5px; font-weight: 700; font-style: italic; color: var(--accent-blue); margin-top: 8px; }
  .inline-link { color: var(--accent-blue); font-style: italic; }
  .more-link { position: absolute; left: 0; top: 143px; font-size: 12.5px; color: var(--dark-text); letter-spacing: 0.3px; }

  .site-footer {
    position: absolute; left: 0; top: 875px; width: 1200px; height: 59px; background: var(--footer-bg);
    font-size: 11px; color: var(--footer-text);
  }
  .site-footer .copyright { position: absolute; left: 142px; top: 22px; }
  .site-footer .legal { position: absolute; right: 143px; top: 22px; text-transform: uppercase; }
  .site-footer .legal a { color: var(--footer-text); }
</style>
</head>
<body>
  <header class="site-header">
    <nav class="main-nav">
      <a class="current" href="#">Home</a>
      <a href="#">About</a><span class="sep">|</span>
      <a href="#">Services</a><span class="sep">|</span>
      <a href="#">Find Property</a><span class="sep">|</span>
      <a href="#">Clients</a><span class="sep">|</span>
      <a href="#">Testimonials</a><span class="sep">|</span>
      <a href="#">Contact</a>
    </nav>
  </header>

  <a class="brand" href="#"><span class="brand-square"></span><span class="brand-name">Reyland &amp; Co</span></a>

  <div class="hero" role="img" aria-label="Waikiki at dusk: lit hotel towers, palm trees, a resort pool and Diamond Head across the bay"></div>
  <div class="slider-dots"><span class="active"></span><span></span><span></span><span></span></div>

  <section class="featured">
    <h2>Featured Property</h2>
    <article class="property-card card-1">
      <div class="photo photo-terrace" role="img" aria-label="Open-air resort terrace with pergola and pool deck"></div>
      <h3>Heading goes here</h3>
      <p>Lorem ipsum dolor sit amet consectetur...</p>
      <a class="details" href="#">DETAILS</a>
    </article>
    <article class="property-card card-2">
      <div class="photo photo-skyline" role="img" aria-label="Aerial view of Waikiki high-rises along turquoise water"></div>
      <h3>Heading goes here</h3>
      <p>Lorem ipsum dolor sit amet consectetur...</p>
      <a class="details" href="#">DETAILS</a>
    </article>
    <article class="property-card card-3">
      <div class="photo photo-beach" role="img" aria-label="Waikiki beach and hotels with Diamond Head in the distance"></div>
      <h3>Heading goes here</h3>
      <p>Lorem ipsum dolor sit amet consectetur...</p>
      <a class="details" href="#">DETAILS</a>
    </article>
  </section>

  <section class="intro">
    <div class="col col-welcome">
      <h2>Welcome Real Estate Boutique</h2>
      <p>Aliquam molestie, mi et imperdiet euismod, dui purus auctor tellus, et interdum lacus lectus et ante. Sed accumsan sollicitudin sapien, sit amet adipiscing turpis gravida ac. In congue, neque ac lobortis volutpat, libero mauris varius mi, vitae suscipit ipsum ligula vitae risus.</p>
      <a class="more-link" href="#">READ MORE</a>
    </div>
    <div class="col col-news">
      <h2>News</h2>
      <p>Sed accumsan sollicitudin sapien, sit amet adipiscing turpis gravida ac. In congue, neque ac lobortis volutpat, libero mauris.......<a class="inline-link" href="#">Read More</a></p>
      <a class="more-link" href="#">READ ALL NEWS</a>
    </div>
    <div class="col col-testimonials">
      <h2>Testimonials</h2>
      <blockquote><span class="quote-mark">&ldquo;</span>Nunc consequat congue nulla eu imperdiet. Donec in est erat, id malesuada turpis......</blockquote>
      <cite>By Owen Tallis</cite>
      <a class="more-link" href="#">READ ALL TESTIMONIALS</a>
    </div>
  </section>

  <footer class="site-footer">
    <span class="copyright">Copyright 2013. Company Name. All Right Reserved</span>
    <span class="legal"><a href="#">Legal Disclaimer</a> &nbsp;|&nbsp; <a href="#">Privacy Policy</a></span>
  </footer>
</body>
</html>
```